Accounting Practice Business Card Design

I have a logo I am happy for you to use in the design of the Business Card.
You can edit and change colours as you please, I am not fixated on it.
I am looking for a modern and clean overall feel for the finished design.

The business is a small accounting practice who thrives on word of mouth referrals and this card will be given to all current and prospect clients.

Industry/Entity Type

Accountant

Contact Information for Business Card

Marcus Elwin
Level 5, 8 Corvale Ridge Road
ASHGROVE RISE VIC 3187
Phone: 9481 3057
Email: melwin@mrfaccountants.com.au
Web: www.mrfaccountants.com.au

Font styles to use
Serif
Sans Serif

Colors
0555a3
3277b5
85acd3
0393ce
33a6d7
85cae6
00a990
33b8a4
9bcb3c

Requirements
Must have
• "The end to your tax problems begin with us"
• "A referral from you is our greatest compliment"
Nice to have
• Modern clean professional

```html
<!DOCTYPE html>
<html lang="en">
<head>
<meta charset="utf-8">
<title>MRF Accountants – Business Card</title>
<link href="https://fonts.googleapis.com/css2?family=Lato:wght@400;700;900&family=Oswald:wght@500&display=swap" rel="stylesheet">
<style>
  :root {
    --backdrop: #3a3a3a;
    --card: #262627;
    --brand-blue: #1a5fb4;
    --band-blue: #2370c8;
    --text-light: #f2f2f2;
    --divider: #8a8a8a;
  }
  * { margin: 0; padding: 0; box-sizing: border-box; }
  html, body {
    width: 1200px;
    height: 900px;
    overflow: hidden;
    background: var(--backdrop);
    font-family: "Lato", sans-serif;
    color: var(--text-light);
  }
  .stage {
    width: 1200px;
    height: 900px;
    display: flex;
    flex-direction: column;
    align-items: center;
    justify-content: center;
    gap: 40px;
  }
  .card {
    position: relative;
    width: 700px;
    height: 400px;
    background: var(--card);
    box-shadow: 0 10px 24px rgba(0,0,0,0.35);
    overflow: hidden;
  }
  .card__band {
    position: absolute;
    left: 0; right: 0; bottom: 0;
    height: 7px;
    background: var(--band-blue);
  }
  .brand {
    color: var(--brand-blue);
    font-family: "Lato", sans-serif;
    font-weight: 900;
    text-align: center;
    line-height: 1;
  }
  .brand__initials {
    display: block;
    font-size: 96px;
    letter-spacing: 2px;
  }
  .brand__word {
    display: block;
    font-size: 30px;
    letter-spacing: 3px;
    margin-top: 4px;
  }
  /* Front */
  .card--front .brand {
    position: absolute;
    left: 0; right: 0;
    top: 88px;
  }
  .tagline {
    position: absolute;
    left: 0; right: 0;
    text-align: center;
    font-size: 17px;
    letter-spacing: 0.6px;
  }
  .card--front .tagline { bottom: 40px; }
  /* Back */
  .card--back .brand {
    position: absolute;
    left: 40px;
    top: 120px;
    width: 300px;
  }
  .card--back .brand__initials { font-size: 82px; }
  .card--back .brand__word { font-size: 26px; }
  .divider {
    position: absolute;
    left: 362px;
    top: 80px;
    width: 1px;
    height: 200px;
    background: var(--divider);
  }
  .contact {
    position: absolute;
    left: 392px;
    top: 82px;
    width: 290px;
  }
  .contact__name {
    font-family: "Oswald", sans-serif;
    font-weight: 500;
    font-variant: small-caps;
    font-size: 30px;
    letter-spacing: 1px;
    color: var(--brand-blue);
    margin-bottom: 18px;
  }
  .contact__address {
    font-size: 17px;
    line-height: 1.4;
    margin-bottom: 10px;
    font-style: normal;
  }
  .contact__row {
    display: flex;
    align-items: center;
    gap: 10px;
    font-size: 17px;
    line-height: 1.55;
  }
  .contact__icon {
    width: 18px;
    height: 18px;
    flex: none;
  }
  .card--back .tagline { bottom: 30px; font-size: 19px; }
</style>
</head>
<body>
<main class="stage">
  <section class="card card--front" aria-label="Card front">
    <div class="brand">
      <span class="brand__initials">MRF</span>
      <span class="brand__word">ACCOUNTANTS</span>
    </div>
    <p class="tagline">A referral from you is our greatest compliment.</p>
    <div class="card__band"></div>
  </section>

  <section class="card card--back" aria-label="Card back">
    <div class="brand">
      <span class="brand__initials">MRF</span>
      <span class="brand__word">ACCOUNTANTS</span>
    </div>
    <div class="divider"></div>
    <div class="contact">
      <h1 class="contact__name">Marcus Elwin</h1>
      <address class="contact__address">Level 5, 8 Corvale Ridge Road<br>Ashgrove Rise Vic 3187</address>
      <div class="contact__row">
        <svg class="contact__icon" viewBox="0 0 24 24" aria-hidden="true"><path d="M6.6 10.8a15.1 15.1 0 0 0 6.6 6.6l2.2-2.2a1 1 0 0 1 1-.25 11.4 11.4 0 0 0 3.6.57 1 1 0 0 1 1 1V20a1 1 0 0 1-1 1A17 17 0 0 1 3 4a1 1 0 0 1 1-1h3.5a1 1 0 0 1 1 1c0 1.25.2 2.45.57 3.6a1 1 0 0 1-.25 1z" fill="#1a5fb4"/></svg>
        <span>9481 3057</span>
      </div>
      <div class="contact__row">
        <svg class="contact__icon" viewBox="0 0 24 24" aria-hidden="true"><rect x="2.5" y="5" width="19" height="14" fill="none" stroke="#1a5fb4" stroke-width="1.6"/><path d="M2.5 5l9.5 8 9.5-8" fill="none" stroke="#1a5fb4" stroke-width="1.6"/></svg>
        <span>melwin@mrfaccountants.com.au</span>
      </div>
      <div class="contact__row">
        <svg class="contact__icon" viewBox="0 0 24 24" aria-hidden="true"><g fill="none" stroke="#1a5fb4" stroke-width="1.5"><circle cx="12" cy="12" r="9.5"/><ellipse cx="12" cy="12" rx="4.2" ry="9.5"/><path d="M2.5 12h19M4 7h16M4 17h16"/></g></svg>
        <span>www.mrfaccountants.com.au</span>
      </div>
    </div>
    <p class="tagline">The end to your tax problems begin with us.</p>
    <div class="card__band"></div>
  </section>
</main>
</body>
</html>
```